Business Card

The design you sent was fine. I just need the logo changed on one side. The back needs to have the text "Vela Norquist Group" next to the log and the words "Counsel Clarity Conviction" in the middle. The front logo needs to have the "Vela Norquist Advisory" logo attached

Colors

Designer to choose colors to be used in the design.

```html
<!DOCTYPE html>
<html lang="en">
<head>
<meta charset="utf-8">
<title>Vela Norquist — Business Card</title>
<link href="https://fonts.googleapis.com/css2?family=Lato:wght@400;700;900&display=swap" rel="stylesheet">
<style>
  :root {
    --backdrop: #4a403b;
    --card: #1c1c1e;
    --accent: #2ab0e0;
    --ink: #f4f4f4;
    --ink-soft: #d8d8d8;
  }
  * { margin: 0; padding: 0; box-sizing: border-box; }
  html, body { width: 1200px; height: 847px; overflow: hidden; }
  body {
    background: var(--backdrop);
    font-family: "Lato", sans-serif;
    position: relative;
  }
  .card {
    position: absolute;
    width: 540px;
    height: 310px;
    background: var(--card);
    border-bottom: 3px solid var(--accent);
    border-right: 2px solid var(--accent);
    box-shadow: 0 18px 40px rgba(0,0,0,0.45);
  }

  /* Back */
  .card-back { left: 60px; top: 100px; }
  .brand-back {
    position: absolute; left: 64px; top: 84px;
    display: flex; align-items: center; gap: 16px;
  }
  .brand-dot-back {
    width: 26px; height: 26px; flex: none;
    border-radius: 50%;
    background: var(--accent);
  }
  .brand-name-back {
    color: var(--ink);
    font-weight: 700;
    font-size: 36px;
    letter-spacing: 0.2px;
    white-space: nowrap;
  }
  .tagline-back {
    position: absolute; left: 106px; top: 142px;
    color: var(--ink-soft);
    font-size: 16px;
    letter-spacing: 1.2px;
    white-space: nowrap;
  }

  /* Front */
  .card-front { left: 600px; top: 440px; }
  .brand-front {
    position: absolute; left: 30px; top: 104px; width: 254px;
  }
  .brand-row { display: flex; align-items: center; gap: 12px; }
  .brand-dot-front {
    width: 18px; height: 18px; flex: none;
    border-radius: 50%;
    background: var(--accent);
  }
  .brand-name-front {
    color: var(--ink);
    font-weight: 700;
    font-size: 21px;
    line-height: 1.15;
  }
  .tagline-front {
    margin-top: 10px;
    padding-left: 30px;
    color: var(--ink-soft);
    font-size: 9px;
    letter-spacing: 0.2px;
    white-space: nowrap;
  }
  .divider {
    position: absolute; left: 300px; top: 60px;
    width: 2px; height: 190px;
    background: var(--accent);
  }
  .contact {
    position: absolute; left: 322px; top: 62px;
    color: var(--ink);
  }
  .person-name {
    color: var(--accent);
    font-weight: 900;
    font-size: 24px;
    letter-spacing: 0.5px;
  }
  .person-role { font-size: 15px; margin-top: 2px; margin-bottom: 10px; }
  .address { font-size: 14px; line-height: 1.35; margin-bottom: 8px; }
  .contact-list { list-style: none; font-size: 14px; }
  .contact-list li { display: flex; align-items: center; gap: 10px; height: 22px; white-space: nowrap; }
  .contact-list svg { width: 14px; height: 14px; flex: none; }
</style>
</head>
<body>

  <section class="card card-back" aria-label="Card back">
    <div class="brand-back">
      <span class="brand-dot-back" aria-hidden="true"></span>
      <span class="brand-name-back">Vela Norquist Group</span>
    </div>
    <p class="tagline-back">Counsel Clarity Conviction</p>
  </section>

  <section class="card card-front" aria-label="Card front">
    <div class="brand-front">
      <div class="brand-row">
        <span class="brand-dot-front" aria-hidden="true"></span>
        <span class="brand-name-front">Vela Norquist Advisory</span>
      </div>
      <p class="tagline-front">Sharp Thinking delivering Practical Lasting Outcomes</p>
    </div>

    <span class="divider" aria-hidden="true"></span>

    <div class="contact">
      <p class="person-name">MARA ELLISON</p>
      <p class="person-role">Founder &amp; CEO</p>
      <p class="address">1234 First Line Address<br>5678 Second Line Address</p>
      <ul class="contact-list">
        <li>
          <svg viewBox="0 0 16 16" aria-hidden="true"><path d="M4 1.5l2.5 3-1.5 1.5a8 8 0 0 0 5 5l1.5-1.5 3 2.5-1.5 2.5C7 14 2 9 1.5 3z" fill="none" stroke="#2ab0e0" stroke-width="1.5" stroke-linejoin="round"/></svg>
          1234567890
        </li>
        <li>
          <svg viewBox="0 0 16 16" aria-hidden="true"><rect x="1" y="3" width="14" height="10" fill="#2ab0e0"/><path d="M1 3l7 6 7-6" fill="none" stroke="#1c1c1e" stroke-width="1.4"/></svg>
          hello@velanorquist.com
        </li>
        <li>
          <svg viewBox="0 0 16 16" aria-hidden="true"><circle cx="8" cy="8" r="6.5" fill="none" stroke="#2ab0e0" stroke-width="1.5"/><path d="M1.5 8h13M8 1.5c-3 3-3 10 0 13M8 1.5c3 3 3 10 0 13" fill="none" stroke="#2ab0e0" stroke-width="1.2"/></svg>
          www.velanorquist.com
        </li>
      </ul>
    </div>
  </section>

</body>
</html>
```